BLENOX - Joining Study and Progress for Fair Opportunity

Brochure is needed for the European Project "BLENOX". We will distribute this flyer during conferences and events to our audiences (mainly academics, researchers, business individuals, policy makers and members of civil society groups) in order to provide the basic information about the project.
The main scope of the project is to support research organisations across Europe to design and implement gender equality plans in order to promote the women’s position of the filed of STEM research.

We are providing a video to explain the layout: https://www.vidstreamhub.example/watch?v=Xk4pR9tLm2Z.
We think size can range from A4-A3.

We are attaching files to provide with concrete information on our requirements:
- BLENOX Brochure Layout_SA.ppt: includes the content we would like to include in the flyer. There is also the URL to the project website
- blenox Logo.zip: the project logo
- Partners Logos.zip: the Logos that will be included
We would like to use colours that belong to the project logo colour range. Regarding the images that you may include in the flyer, we wouldn't like to propose any because we do not want to limitate your imagination. We have some at the website https://blenox-project.example/. They could be diverse (age, race, gender, etc.) relevant to women and men.

```html
<!DOCTYPE html>
<html lang="en">
<head>
<meta charset="utf-8">
<title>BLENOX – Brochure Spread</title>
<link rel="stylesheet" href="https://fonts.googleapis.com/css2?family=Montserrat:wght@300;400;500;600;700&display=swap">
<style>
  :root{
    --yellow:#E8B125;
    --yellow-soft:#F2C75A;
    --purple:#4A4EA8;
    --purple-light:#8A8DD8;
    --ink:#5a5a5a;
    --paper:#ffffff;
    --photo-a:#9a9890;
    --photo-b:#c9c6bd;
  }
  *{box-sizing:border-box;margin:0;padding:0}
  html,body{width:1200px;height:833px;overflow:hidden;background:#e6e6e6}
  body{font-family:"Montserrat",sans-serif;color:var(--ink)}
  .spread{position:relative;width:1200px;height:833px;background:var(--paper)}
  .shapes{position:absolute;inset:0;width:1200px;height:833px}
  .spine{position:absolute;left:599px;top:0;width:2px;height:833px;background:linear-gradient(90deg,rgba(0,0,0,.08),rgba(0,0,0,0))}
  .block{position:absolute}
  h2{font-weight:300;letter-spacing:.04em}
  p{font-size:10.5px;line-height:1.45}

  .goal{left:56px;top:70px;width:380px;color:#fff}
  .goal h2{font-size:30px;margin-bottom:12px}
  .goal p{color:#fff;margin-bottom:4px}

  .consortium{left:56px;top:390px;width:380px}
  .consortium h2{font-size:30px;color:var(--yellow);margin-bottom:10px}

  .group-label{position:absolute;font-size:8px;color:var(--purple-light);letter-spacing:.04em}
  .partner{position:absolute;display:flex;align-items:center;gap:5px;font-size:9px;font-weight:600;color:var(--purple);line-height:1.15}
  .partner .mark{flex:none;width:14px;height:14px;background:var(--purple)}
  .partner .mark.round{border-radius:50%;background:var(--yellow)}

  .hubs{left:628px;top:36px;width:360px}
  .hubs h2{font-size:21px;color:var(--purple);margin-bottom:8px}
  .hubs ul{list-style:none;margin:2px 0 4px}
  .hubs li{font-size:10.5px;font-weight:700;color:var(--purple-light);line-height:1.35}

  .impact{left:640px;top:318px;width:240px;color:#fff}
  .impact h2{font-size:24px;margin-bottom:6px}
  .impact p{font-size:9.5px;color:#fff}

  .aims{position:absolute;left:640px;top:555px;width:540px;display:flex;justify-content:space-between}
  .aim{width:165px;text-align:center;color:var(--purple);font-size:9.5px;line-height:1.4}
  .aim svg{display:block;margin:0 auto 8px}
  .footnote{position:absolute;right:44px;bottom:40px;font-size:7px;color:var(--purple)}
</style>
</head>
<body>
<main class="spread">
  <svg class="shapes" viewBox="0 0 1200 833" aria-hidden="false">
    <!-- left page top band -->
    <path d="M0,0 H600 V230 Q300,290 0,360 Z" fill="var(--yellow)"/>
    <path d="M420,0 H600 V230 Q520,240 430,262 Z" fill="var(--yellow-soft)" opacity=".7"/>
    <!-- photo area across spine -->
    <path role="img" aria-label="Photo area: two researchers working on laptops at a table, seen from above, on a floor with coloured taped lines"
      d="M430,300 Q600,250 790,228 H1200 V505 Q900,470 640,560 Q540,600 478,585 Z" fill="url(#photoTone)"/>
    <!-- top-right purple panel -->
    <rect x="1010" y="0" width="190" height="232" fill="var(--purple)"/>
    <!-- impact panel -->
    <polygon points="612,300 968,255 905,560 640,540" fill="var(--purple)" opacity=".88"/>
    <!-- lower yellow bands -->
    <path d="M600,560 Q820,470 1200,482 V833 H600 Z" fill="var(--yellow)"/>
    <path d="M478,585 Q545,600 600,575 V833 H535 Q505,700 478,585 Z" fill="var(--yellow-soft)"/>
    <defs>
      <linearGradient id="photoTone" x1="0" y1="0" x2="1" y2="1">
        <stop offset="0" stop-color="var(--photo-b)"/>
        <stop offset="1" stop-color="var(--photo-a)"/>
      </linearGradient>
    </defs>
  </svg>
  <div class="spine"></div>

  <section class="block goal">
    <h2>The Goal</h2>
    <p>BLENOX project supports 7 RPOs and 2 RFOs, that are in an initial stage, to develop Gender Equality Plans (GEPs) and engage the local Innovation Hubs to transfer the gained knowledge beyond academia.</p>
    <p>The project goal is to make research organizations more gender equal by increasing the number of female researchers in STEM, improving their careers prospects and integrating a gender dimension in research.</p>
  </section>

  <section class="block consortium">
    <h2>Consortium</h2>
    <p>BLENOX consists of 7 Research Performing Organisations (RPOs) and 7 Research Funding Organisations (RFOs) to develop a GEP covering a wide area around Europe, including 8 EU countries, Turkey and Georgia. The project also includes 2 SMEs undertaking project coordination (Vexa Labs) and the scientific management (Lagoon Works) and a professional association (Young Scholars Forum) to expand the project results.</p>
  </section>

  <span class="group-label" style="left:290px;top:560px">RPOs</span>
  <div class="partner" style="left:320px;top:585px"><span class="mark"></span>FEC Delmar</div>
  <div class="partner" style="left:430px;top:575px"><span class="mark"></span>Tarnov Technical<br>University</div>
  <div class="partner" style="left:200px;top:625px"><span class="mark round"></span>Università<br>di Morvano</div>
  <div class="partner" style="left:320px;top:630px"><span class="mark round"></span>Aegis Polytechnic<br>Institute</div>
  <div class="partner" style="left:60px;top:680px"><span class="mark"></span>Karvel<br>University</div>
  <div class="partner" style="left:190px;top:690px"><span class="mark round"></span>Orsa Bio<br>Institute</div>
  <div class="partner" style="left:60px;top:735px"><span class="mark"></span>Université Libre<br>de Varenne</div>

  <span class="group-label" style="left:470px;top:645px">Professional Association</span>
  <div class="partner" style="left:490px;top:670px"><span class="mark round"></span>Young Scholars<br>Forum</div>
  <span class="group-label" style="left:380px;top:700px">SMEs</span>
  <div class="partner" style="left:330px;top:725px"><span class="mark"></span>Vexa Labs</div>
  <div class="partner" style="left:440px;top:720px"><span class="mark round"></span>Lagoon Works</div>

  <span class="group-label" style="left:250px;top:765px">RFOs</span>
  <div class="partner" style="left:150px;top:790px"><span class="mark round"></span>Ardea Funding<br>Agency</div>
  <div class="partner" style="left:290px;top:785px"><span class="mark"></span>Mtkvari Science<br>Foundation</div>

  <section class="block hubs">
    <h2>BLENOX Research &amp; Innovation Hubs</h2>
    <p>The RPOs/RFOs of the project establish local Research &amp; Innovation Hubs with the following stakeholders:</p>
    <ul>
      <li>Academia and Universities</li>
      <li>Industry and Business</li>
      <li>Government &amp; Public Sector</li>
      <li>Civil society</li>
    </ul>
    <p>The strategic synergies stimulate dialogues to identify gaps and challenges related to gender inequalities at the different levels of the education-research-transfer to market and innovation chain.</p>
  </section>

  <section class="block impact">
    <h2>Impact</h2>
    <p>BLENOX vision is to enhance the gender balance in STEM fields and promote a greater engagement of female researchers with research and innovation, contributing to the ERA<sup>1</sup> priorities on Gender Equality and stimulating a dialogue and collaboration between academia, public authorities, professionals and industry players in order to tackle gender inequalities across the research-transfer-to-market chain.</p>
  </section>

  <section class="aims">
    <div class="aim">
      <svg width="34" height="34" viewBox="0 0 34 34" fill="none" stroke="var(--purple)" stroke-width="1.6"><circle cx="11" cy="7" r="3.5"/><path d="M5 32V16h12v16M11 22v10M17 18l6-6M23 4v12M23 4h8v5h-8"/></svg>
      Remove barriers to the recruitment, retention and career progression of female researchers
    </div>
    <div class="aim">
      <svg width="36" height="34" viewBox="0 0 36 34" fill="none" stroke="var(--purple)" stroke-width="1.6"><rect x="6" y="2" width="24" height="15"/><path d="M11 13v-4M16 13V7M21 13v-5M26 13V9"/><circle cx="8" cy="23" r="3"/><circle cx="18" cy="23" r="3"/><circle cx="28" cy="23" r="3"/><path d="M3 32q5-6 10 0M13 32q5-6 10 0M23 32q5-6 10 0"/></svg>
      Integrate the gender dimension in research and innovation content, improving the quality and societal relevance of produced knowledge, technologies and innovations.
    </div>
    <div class="aim">
      <svg width="36" height="34" viewBox="0 0 36 34" fill="none" stroke="var(--purple)" stroke-width="1.6"><path d="M4 14h28M18 14v16M12 30h12M18 14l-4-4h8z"/><circle cx="9" cy="7" r="3"/><circle cx="27" cy="7" r="3"/></svg>
      Improve the gender balance in decision-making bodies
    </div>
  </section>

  <p class="footnote">1 Communication of the Continental Research Board of the 17.07.2017</p>
</main>
</body>
</html>
```